Creative designer wanted for unique pet treats product packaging!

My company is "Tailwag Pantry!" and we're a new and upcoming premium pet treat company. We are different than the rest as we have core values that really stand out and that we're VERY passionate about. They are the following:
HEALTHY-All of our ingredients are fresh and wholesome for dogs. Each has unique health benefits for dogs and there is never any filler-just the good stuff.
AMOUNT OF INGREDIENTS-Most of dog treats have large lists of ingredients and often many of those are difficult to pronounce or people have to look up what they even are. Often there is lot of "filler". We pride ourselves on just having a few ingredients or less. Every ingredient can easily be pronounced, recognized and are commonly consumed by humans in regular meals.
GIVING BACK- We donate a portion of the proceeds of every bag to go to hand selected, accredited and legit animals charities and rescues.
ENVIRONMENT- We strongly care about the environment which is why our bags are compostable. Just simply remove the zipper and track then put the bag in a composting bin. Easy as that. (We have attached a "how to compost your bag in 2 simple steps" image that we would like shown on the bags.
Our initial product is Maple Sage Crunchy Bark-ley Bites. The ingredients are: Coconut oil, dill, and sweet potato.
We want a design that embodies our values. As well, we have attached "our story" that describes the company and what we are about to consumers. We would like to have it put on the package, but if it cannot be done, then just the meat and potatoes of the message.
A good example for recognition is the attached cake mix as it's simple, portrays the product nicely and when seen from afar-it is easily identified.
*We would like to have a window on the bag that is similar to our paw and leaf logo.
We would also like to see the color green on the package.
Bag specifics are:
Size: 250g OPTIMIZED
Dimensions Inches: 6.15''x9.41''x3.50''
Dimensions mm : 156x239x89
Type: Stand-Up Pouch with Zip (PLOW)
COMPOSTABLE
Material: 100NK MATTE/70NKA/3mil BIOPBS
CMYKW

```html
<!DOCTYPE html>
<html lang="en">
<head>
<meta charset="utf-8">
<title>Tailwag Pantry! – Maple Sage Crunchy Bark-ley Bites</title>
<link rel="stylesheet" href="https://fonts.googleapis.com/css2?family=Anton&family=Kaushan+Script&family=Montserrat:wght@600&family=Oswald:wght@500&display=swap">
<style>
  :root {
    --page: #ffffff;
    --band: #bde66a;
    --panel-top: #e8f59a;
    --panel-bottom: #f6eeb4;
    --brown: #7b4a2b;
    --green-bright: #b8ec3e;
    --green-pale: #cdef6e;
    --green-mid: #8ed93a;
    --green-dark: #2f6b1c;
    --window-line: #9fdc36;
    --treat-light: #e8b77f;
    --treat-dark: #b8763f;
  }
  * { box-sizing: border-box; margin: 0; padding: 0; }
  html, body { width: 1200px; height: 892px; overflow: hidden; background: var(--page); }
  .canvas { position: relative; width: 1200px; height: 892px; }

  .pouch-front {
    position: absolute; left: 310px; top: 27px; width: 580px; height: 838px;
    background: linear-gradient(180deg, var(--panel-top) 0%, #eef5a8 45%, var(--panel-bottom) 100%);
    overflow: hidden;
  }
  .leaf-band { position: absolute; left: 0; top: 0; width: 580px; height: 200px; }
  .tree-backdrop {
    position: absolute; left: 0; bottom: 0; width: 580px; height: 300px;
    background: linear-gradient(180deg, rgba(240,222,150,0) 0%, rgba(232,214,140,0.55) 100%);
  }

  .corner-note {
    position: absolute; top: 24px; width: 80px;
    font-family: "Oswald", sans-serif; font-weight: 500;
    font-size: 16px; line-height: 1.05; color: var(--brown);
    text-align: center; text-transform: uppercase;
  }
  .corner-note--left { left: 22px; }
  .corner-note--right { right: 22px; }

  .brand {
    position: absolute; top: 144px; left: 0; width: 100%;
    display: flex; justify-content: center; align-items: center; gap: 8px;
  }
  .brand-dot { width: 14px; height: 14px; border-radius: 50%; background: var(--brown); }
  .brand-name {
    font-family: "Montserrat", sans-serif; font-weight: 600;
    font-size: 25px; color: var(--brown);
  }

  .script {
    font-family: "Kaushan Script", cursive;
    position: absolute; left: 0; width: 100%; text-align: center; line-height: 1;
  }
  .tagline { top: 202px; font-size: 30px; color: var(--brown); }
  .flavour {
    position: absolute; left: 0; width: 100%; text-align: center;
    font-family: "Anton", sans-serif; top: 238px; font-size: 52px;
    letter-spacing: 1px; color: var(--green-bright); line-height: 1;
  }
  .product-name {
    position: absolute; left: 0; width: 100%; text-align: center;
    font-family: "Anton", sans-serif; top: 290px; font-size: 104px;
    letter-spacing: 2px; color: var(--green-pale); line-height: 1;
  }
  .style-word { top: 282px; font-size: 28px; color: var(--green-mid); z-index: 2; }
  .format-word { top: 392px; font-size: 40px; color: var(--green-dark); z-index: 2; }

  .ingredient-art {
    position: absolute; left: 6px; top: 412px; width: 120px; height: 140px;
    border-radius: 50% 50% 46% 46%;
    background: linear-gradient(160deg, #d9b26a 0%, #a9733f 55%, #7a4c2a 100%);
  }

  .treat-window {
    position: absolute; left: 140px; top: 452px; width: 320px; height: 282px;
    border: 5px solid var(--window-line); border-radius: 44px;
    background: radial-gradient(circle at 40% 45%, var(--treat-light) 0%, #d99a5c 55%, var(--treat-dark) 100%);
  }

  .size-word { top: 748px; font-size: 34px; color: var(--green-mid); }
  .claim {
    position: absolute; top: 796px; left: 0; width: 100%; text-align: center;
    font-family: "Oswald", sans-serif; font-weight: 500; font-size: 15px;
    color: var(--brown); text-transform: uppercase;
  }
  .compost-note {
    position: absolute; top: 820px; left: 0; width: 100%; text-align: center;
    font-family: Arial, Helvetica, sans-serif; font-size: 10px; color: #3a2a1a;
  }
</style>
</head>
<body>
<main class="canvas">
  <section class="pouch-front">
    <div class="tree-backdrop" role="img" aria-label="Soft pine tree silhouettes in pale sand tones"></div>

    <svg class="leaf-band" viewBox="0 0 580 200" role="img" aria-label="Green band with a scattered leaf pattern">
      <path d="M0 0 H580 V150 C560 185 520 180 505 160 C470 190 430 170 420 150 C400 140 380 145 370 160 L210 160 C195 140 170 140 155 155 C130 185 90 185 70 160 C50 190 15 190 0 165 Z" fill="var(--band)"/>
    </svg>

    <p class="corner-note corner-note--left">Hand<br>Crafted<br>Product</p>
    <p class="corner-note corner-note--right">Net<br>Weight<br>130<sup>g</sup></p>

    <div class="brand">
      <span class="brand-dot"></span>
      <span class="brand-name">Tailwag Pantry!</span>
    </div>

    <p class="script tagline">Naturally Delicious</p>
    <p class="flavour">MAPLE SAGE</p>
    <p class="product-name">BARK-LEY</p>
    <p class="script style-word">Crunchy</p>
    <p class="script format-word">Bites</p>

    <div class="ingredient-art" role="img" aria-label="Illustration of wheat stalks, a split coconut and sweet potato pieces"></div>

    <div class="treat-window" role="img" aria-label="Clear window showing the golden bite-size treats inside"></div>

    <p class="script size-word">Bite Size</p>
    <p class="claim">Made from natural ingredients-environment friendly</p>
    <p class="compost-note">ALL OUR BAGS ARE COMPOSTABLE (SEE BACK FOR DETAILS)</p>
  </section>
</main>
</body>
</html>
```